Business Card Design Project

I am seeking a business card for my life coaching career. I specialize in coaching executives and entrepreneurs. Consciousness plays a key role in my practice.
Updates

I would like to see different fonts -I don't like the way the capital J looks. I only want my name once on the card, on the front. I like everything centered on the front, with a white background, grey and green on the front; and the same grey on the back with bullet points next to each quality; centered. I like a subtle shadow of the mountains behind the text on the back of the card. I don't want the mountains on either side to be too big. Thank you.

Target Market(s)

Middle age business owners/executives

Industry/Entity Type

Business

Contact Information for Business Card

The front design is my name and a mountain logo. I want to have my name prominently shown.

Requirements
Must have
• Front of card:
• My name prominent sized font
• Helping clients lead more fulfilling lives;
• Executive Life Coach
• 415-362-4807
• pkrelt4@mailvane.net
• Back of Card:
• Providing Unparalleled support
• Providing a safe place to grow in self-awareness
• 20+ years entrepreneurial experience
• Trust
• Integrity
Nice to have
• Easy to read font; warm colors reflecting a masculine personality.

```html
<!DOCTYPE html>
<html lang="en">
<head>
<meta charset="utf-8">
<title>Neil Harrow – Business Card</title>
<link rel="stylesheet" href="https://fonts.googleapis.com/css2?family=Alegreya+SC:wght@500&family=Alegreya:wght@500&family=Jost:wght@300&display=swap">
<style>
  :root {
    --page-bg: #ffffff;
    --card-bg: #ffffff;
    --card-edge: #1e1e1e;
    --brand-green: #5a6e3c;
    --ink: #1f1f1f;
  }
  html, body {
    margin: 0;
    padding: 0;
    width: 1200px;
    height: 1000px;
    overflow: hidden;
    background: var(--page-bg);
  }
  .canvas {
    position: relative;
    width: 1200px;
    height: 1000px;
  }
  .card {
    position: absolute;
    left: 75px;
    top: 200px;
    width: 1050px;
    height: 599px;
    border: 1px solid var(--card-edge);
    background: var(--card-bg);
  }
  .rule {
    position: absolute;
    top: 254px;
    height: 2px;
    background: var(--brand-green);
  }
  .rule--left { left: 0; width: 226px; }
  .rule--right { right: 0; width: 224px; }
  .name {
    position: absolute;
    left: 0;
    right: 0;
    top: 208px;
    margin: 0;
    text-align: center;
    font-family: "Alegreya SC", Georgia, serif;
    font-weight: 500;
    font-size: 84px;
    line-height: 1;
    letter-spacing: 1px;
    color: var(--brand-green);
  }
  .role {
    position: absolute;
    left: 0;
    right: 0;
    top: 306px;
    margin: 0;
    text-align: center;
    font-family: "Alegreya", Georgia, serif;
    font-weight: 500;
    font-size: 29px;
    color: var(--ink);
  }
  .tagline {
    position: absolute;
    left: 0;
    right: 0;
    top: 352px;
    margin: 0;
    text-align: center;
    font-family: "Alegreya", Georgia, serif;
    font-weight: 500;
    font-size: 25px;
    color: var(--ink);
  }
  .contact {
    position: absolute;
    left: 0;
    right: 0;
    top: 475px;
    margin: 0;
    text-align: center;
    font-family: "Jost", "Futura", sans-serif;
    font-weight: 300;
    font-size: 38px;
    color: var(--ink);
  }
</style>
</head>
<body>
  <main class="canvas">
    <section class="card">
      <div class="rule rule--left"></div>
      <div class="rule rule--right"></div>
      <h1 class="name">NEIL HARROW</h1>
      <p class="role">Executive Life Coach</p>
      <p class="tagline">Helping clients lead more fulfilling lives</p>
      <p class="contact">415-362-4807 | pkrelt4@mailvane.net</p>
    </section>
  </main>
</body>
</html>
```